Quiet Willow Business Cards
Quiet Willow Body and Beauty Therapies
Bright & Fun-filled
Noreen Baptiste
Owner/Operator OPV, DRAM, NOPREX, VERTUMA
Bermuda
brightvanspa@examplemail.net
quietwillowvisits.com
Please design a business card with rounded corners Only the logo goes on the front. Name and additional info goes on the back Coloured background please
Noreen Baptiste (in bold print) Owner/Operator OPV, DRAM, NOPREX, VERTUMA mobile: 441-555-0148 email: brightvanspa@examplemail.net web site: quietwillowvisits.com Spa therapies in the comfort of home

```html
<!DOCTYPE html>
<html lang="en">
<head>
<meta charset="utf-8">
<title>Quiet Willow Stationery</title>
<link rel="stylesheet" href="https://fonts.googleapis.com/css2?family=Cormorant+Garamond:wght@600&family=Open+Sans:wght@400;700&display=swap">
<style>
  :root {
    --backdrop: #e9e6e1;
    --paper: #ffffff;
    --green: #6f9a1f;
    --green-dark: #4f7410;
    --green-light: #a6c750;
    --ink: #555b4a;
    --flap-dark: #1b1b1b;
    --watermark: #eef1e8;
  }
  * { box-sizing: border-box; margin: 0; padding: 0; }
  html, body { width: 1200px; height: 492px; overflow: hidden; }
  body { background: var(--backdrop); font-family: "Open Sans", sans-serif; color: var(--ink); }
  .stationery { position: relative; width: 1200px; height: 492px; }

  .piece { position: absolute; background: var(--paper); overflow: hidden; box-shadow: 0 2px 6px rgba(0,0,0,.18); }
  .card { width: 202px; height: 118px; border-radius: 10px; }
  .card--green { background: linear-gradient(135deg, var(--green-light), var(--green) 55%, var(--green-dark)); }

  .wordmark { display: flex; flex-direction: column; align-items: center; gap: 2px; }
  .wordmark__row { display: flex; align-items: center; gap: 6px; }
  .wordmark__dot { width: 10px; height: 10px; border-radius: 50%; background: var(--green); }
  .wordmark__name { font-family: "Cormorant Garamond", serif; font-weight: 600; color: var(--green); line-height: 1; white-space: nowrap; }
  .wordmark__tag { font-size: 6px; color: var(--ink); letter-spacing: .3px; white-space: nowrap; }
  .on-green .wordmark__name, .on-green .wordmark__tag { color: #fff; }
  .on-green .wordmark__dot { background: #fff; }

  .contact { font-size: 6px; line-height: 1.45; color: var(--ink); white-space: nowrap; }
  .contact strong { font-size: 7px; color: var(--green-dark); }
  .on-green .contact, .on-green .contact strong { color: #fff; }
  .contact--small { font-size: 5px; }

  .letterhead .wordmark__dot { width: 8px; height: 8px; }
  .letterhead .wordmark__row { gap: 4px; }
  .letterhead .wordmark__tag { font-size: 5px; }

  .swoosh { position: absolute; left: 0; bottom: 0; }
  .watermark { position: absolute; border-radius: 50%; background: var(--watermark); }
</style>
</head>
<body>
<main class="stationery">

  <!-- Business card back: white with corner swoosh -->
  <section class="piece card" style="left:12px;top:20px;">
    <svg class="swoosh" width="202" height="118" viewBox="0 0 202 118" aria-hidden="true">
      <path d="M0 70 Q40 112 202 100 L202 118 L0 118 Z" fill="var(--green)"/>
    </svg>
    <div class="contact" style="position:absolute;left:10px;top:10px;">
      <strong>Noreen Baptiste</strong><br>Owner/Operator<br>OPV, DRAM, NOPREX, VERTUMA
    </div>
    <div class="wordmark" style="position:absolute;left:60px;top:38px;">
      <div class="wordmark__row"><span class="wordmark__dot"></span><span class="wordmark__name" style="font-size:20px;">Quiet Willow</span></div>
      <span class="wordmark__tag">Body and Beauty Therapies</span>
    </div>
  </section>

  <!-- Business card back: white with lower band -->
  <section class="piece card" style="left:228px;top:20px;">
    <div class="wordmark" style="position:absolute;left:40px;top:10px;">
      <div class="wordmark__row"><span class="wordmark__dot"></span><span class="wordmark__name" style="font-size:20px;">Quiet Willow</span></div>
      <span class="wordmark__tag">Body and Beauty Therapies</span>
    </div>
    <div class="contact" style="position:absolute;left:12px;top:50px;">
      <strong>Noreen Baptiste</strong> &nbsp;Owner/Operator<br>mobile: 441-555-0148<br>brightvanspa@examplemail.net<br>quietwillowvisits.com
    </div>
    <svg class="swoosh" width="202" height="118" viewBox="0 0 202 118" aria-hidden="true">
      <path d="M0 104 Q100 96 202 108 L202 118 L0 118 Z" fill="var(--green)"/>
    </svg>
  </section>

  <!-- Card front: green -->
  <section class="piece card card--green on-green" style="left:12px;top:160px;">
    <div class="wordmark" style="position:absolute;left:0;right:0;top:44px;">
      <div class="wordmark__row"><span class="wordmark__dot"></span><span class="wordmark__name" style="font-size:22px;">Quiet Willow</span></div>
      <span class="wordmark__tag">Body and Beauty Therapies</span>
    </div>
  </section>

  <!-- Card front: white -->
  <section class="piece card" style="left:228px;top:160px;">
    <div class="wordmark" style="position:absolute;left:0;right:0;top:44px;">
      <div class="wordmark__row"><span class="wordmark__dot"></span><span class="wordmark__name" style="font-size:22px;">Quiet Willow</span></div>
      <span class="wordmark__tag">Body and Beauty Therapies</span>
    </div>
  </section>

  <!-- Card back: green -->
  <section class="piece card card--green on-green" style="left:12px;top:305px;">
    <div class="wordmark" style="position:absolute;left:0;right:0;top:26px;">
      <div class="wordmark__row"><span class="wordmark__dot"></span><span class="wordmark__name" style="font-size:24px;">Quiet Willow</span></div>
      <span class="wordmark__tag">Body and Beauty Therapies</span>
    </div>
    <div class="contact" style="position:absolute;left:0;right:0;top:74px;text-align:center;">Spa therapies in the comfort of home</div>
  </section>

  <!-- Card back: white -->
  <section class="piece card" style="left:228px;top:305px;">
    <div class="wordmark" style="position:absolute;left:0;right:0;top:26px;">
      <div class="wordmark__row"><span class="wordmark__dot"></span><span class="wordmark__name" style="font-size:24px;">Quiet Willow</span></div>
      <span class="wordmark__tag">Body and Beauty Therapies</span>
    </div>
    <div class="contact" style="position:absolute;left:0;right:0;top:74px;text-align:center;">Spa therapies in the comfort of home</div>
  </section>

  <!-- Letterhead -->
  <section class="piece letterhead" style="left:440px;top:30px;width:204px;height:428px;">
    <div class="wordmark" style="position:absolute;left:10px;top:14px;align-items:flex-start;">
      <div class="wordmark__row"><span class="wordmark__dot"></span><span class="wordmark__name" style="font-size:15px;">Quiet Willow</span></div>
      <span class="wordmark__tag">Body and Beauty Therapies</span>
    </div>
    <div class="contact contact--small" style="position:absolute;right:8px;top:15px;">
      mobile: 441-555-0148<br>brightvanspa@examplemail.net<br>quietwillowvisits.com
    </div>
    <div class="watermark" style="left:37px;top:140px;width:130px;height:130px;"></div>
    <svg class="swoosh" width="204" height="428" viewBox="0 0 204 428" aria-hidden="true">
      <path d="M0 400 Q110 404 204 380 L204 428 L0 428 Z" fill="var(--green)"/>
    </svg>
  </section>

  <!-- Envelope back with dark flap -->
  <section class="piece envelope" style="left:748px;top:28px;width:440px;height:170px;">
    <svg width="440" height="170" viewBox="0 0 440 170" style="position:absolute;left:0;top:0;" aria-hidden="true">
      <path d="M0 0 H440 V28 L236 92 Q220 97 204 92 L0 28 Z" fill="var(--flap-dark)"/>
    </svg>
    <div class="wordmark" style="position:absolute;left:0;right:0;top:14px;">
      <div class="wordmark__row"><span class="wordmark__dot"></span><span class="wordmark__name" style="font-size:16px;">Quiet Willow</span></div>
    </div>
  </section>

  <!-- Envelope back, white -->
  <section class="piece envelope" style="left:748px;top:142px;width:440px;height:170px;">
    <svg width="440" height="170" viewBox="0 0 440 170" style="position:absolute;left:0;top:0;" aria-hidden="true">
      <path d="M0 0 L204 62 Q220 67 236 62 L440 0" fill="none" stroke="#d8d8d8" stroke-width="1"/>
    </svg>
    <div class="wordmark" style="position:absolute;left:0;right:0;top:10px;">
      <div class="wordmark__row"><span class="wordmark__dot"></span><span class="wordmark__name" style="font-size:16px;">Quiet Willow</span></div>
    </div>
  </section>

  <!-- Envelope front with green band -->
  <section class="piece envelope" style="left:598px;top:250px;width:352px;height:186px;">
    <svg width="352" height="186" viewBox="0 0 352 186" style="position:absolute;left:0;top:0;" aria-hidden="true">
      <path d="M0 0 H352 V34 Q200 14 0 44 Z" fill="var(--green)"/>
      <path d="M0 186 V166 Q60 176 120 186 Z" fill="var(--green)"/>
    </svg>
    <div class="wordmark on-green" style="position:absolute;left:0;right:0;top:6px;">
      <div class="wordmark__row"><span class="wordmark__dot"></span><span class="wordmark__name" style="font-size:17px;">Quiet Willow</span></div>
    </div>
    <div class="contact" style="position:absolute;left:14px;top:122px;">
      mobile: 441-555-0148<br>brightvanspa@examplemail.net<br>quietwillowvisits.com
    </div>
  </section>

</main>
</body>
</html>
```